Simple landing page/Web presence for boutique Fund Manager, Brellow Funds Management

We need a website presence for our funds management business. All we need is a simple landing page with some "text" about us and a link /button to our Fund Due diligence portal. the "text" we would like to see is: "Brellow Funds Management Pty Ltd. Its Trustee is Tindale Fund Services Ltd - also based in Sydney. Tindale is the holder of an Australian Financial Services License (no.731052) whilst Brellow Funds Management operates under a Corporate Authorised Representation from Tindale."

We have the attached logo

```html
<!DOCTYPE html>
<html lang="en">
<head>
<meta charset="utf-8">
<title>Brellow Funds Management</title>
<link href="https://fonts.googleapis.com/css2?family=Montserrat:wght@400;500;600&display=swap" rel="stylesheet">
<style>
  :root {
    --bg: #161616;
    --ink: #ffffff;
    --ink-dark: #222222;
  }
  * { margin: 0; padding: 0; box-sizing: border-box; }
  html, body {
    width: 1200px;
    height: 675px;
    overflow: hidden;
    background: var(--bg);
    font-family: "Montserrat", sans-serif;
    color: var(--ink);
  }
  .page {
    position: relative;
    width: 1200px;
    height: 675px;
  }
  .brand {
    position: absolute;
    top: 118px;
    left: 0;
    width: 1200px;
    display: flex;
    justify-content: center;
    align-items: center;
    gap: 16px;
  }
  .brand-mark {
    width: 26px;
    height: 26px;
    background: var(--ink);
  }
  .brand-name {
    font-size: 34px;
    font-weight: 600;
    letter-spacing: 1px;
    color: var(--ink);
  }
  .about {
    position: absolute;
    top: 250px;
    left: 240px;
    width: 720px;
    text-align: center;
    font-size: 19.3px;
    font-weight: 500;
    line-height: 42px;
  }
  .actions {
    position: absolute;
    top: 452px;
    left: 0;
    width: 1200px;
    display: flex;
    justify-content: center;
    gap: 24px;
  }
  .button {
    display: flex;
    align-items: center;
    justify-content: center;
    width: 218px;
    height: 51px;
    font-size: 19px;
    font-weight: 500;
    letter-spacing: 2px;
    text-decoration: none;
  }
  .button--outline {
    border: 2px solid var(--ink);
    color: var(--ink);
  }
  .button--solid {
    background: var(--ink);
    color: var(--ink-dark);
  }
  .footer {
    position: absolute;
    top: 630px;
    left: 0;
    width: 1200px;
    text-align: center;
    font-size: 16px;
    font-weight: 500;
    letter-spacing: 3px;
  }
</style>
</head>
<body>
  <main class="page">
    <header class="brand">
      <span class="brand-mark"></span>
      <span class="brand-name">Brellow Funds Management</span>
    </header>
    <p class="about">Brellow Funds Management Pty Ltd. Its Trustee is Tindale Fund Services Ltd - also based in Sydney. Tindale is the holder of an Australian Financial Services License (no.731052) whilst Brellow Funds Management operates under a Corporate Authorised Representation from Tindale.</p>
    <nav class="actions">
      <a class="button button--outline" href="#">DUE DILIGENCE</a>
      <a class="button button--solid" href="#">CONTACT US</a>
    </nav>
    <footer class="footer">© 2020 · Brellow funds management pvt limited</footer>
  </main>
</body>
</html>
```